Laundry pickup and delivery flyer "Fold Harbor laundry"

I need a flyer "8.5"x11" that tells customers about our pickup and delivery laundry service. our website address is: www.foldharborlaundry.example The flyer should be front and back.

Font styles to use
Sans Serif

Colors
0094D4
00A9DD
6FCCEA
C7EBF8
E9F6FB

```html
<!DOCTYPE html>
<html lang="en">
<head>
<meta charset="utf-8">
<title>Fold Harbor Laundry – Pickup &amp; Delivery Flyer</title>
<link rel="stylesheet" href="https://fonts.googleapis.com/css2?family=Open+Sans:ital,wght@0,400;0,600;0,700;0,800;1,600&family=Montserrat:wght@500;600&display=swap">
<style>
:root{
  --navy:#0a2a8f;
  --royal:#1638c9;
  --brand:#0094D4;
  --sky:#00A9DD;
  --aqua:#6FCCEA;
  --mist:#C7EBF8;
  --foam:#E9F6FB;
  --teal:#46ecd8;
  --ice:#a8f6ee;
  --yellow:#ffec3d;
  --ink:#111;
}
*{box-sizing:border-box;margin:0;padding:0}
html,body{width:1200px;height:756px;overflow:hidden;background:#fff}
body{font-family:"Open Sans",Arial,sans-serif;position:relative}
.side-label{position:absolute;top:-4px;font-size:20px;color:#111;font-weight:400;letter-spacing:.5px;transform:translateX(-50%)}
.panel{position:absolute;top:19px;height:737px;overflow:hidden;background:#fff}
.front{left:0;width:570px;border:1px solid #bbb}
.back{left:630px;width:570px;border:1px solid #bbb}
.layer{position:absolute;left:0;top:0}
.photo{position:absolute}
.brand-name{position:absolute;font-family:"Open Sans",Arial,sans-serif;font-weight:800;color:var(--royal);white-space:nowrap;display:flex;align-items:center}
.brand-dot{border-radius:50%;background:var(--sky);display:inline-block}
.front .brand-name{left:26px;top:68px;font-size:31px;gap:10px}
.front .brand-dot{width:18px;height:18px}
.outsource{position:absolute;right:18px;top:248px;text-align:right;color:#fff}
.outsource h2{font-family:"Montserrat",Arial,sans-serif;font-weight:500;font-size:33px;letter-spacing:1px;text-shadow:0 0 2px var(--navy),0 0 2px var(--navy)}
.outsource p{font-style:italic;font-weight:600;font-size:19px;color:#fff;margin-top:-4px;text-shadow:0 0 2px #333,1px 1px 2px #333}
.hero{position:absolute;left:28px;top:338px;color:#fff}
.hero h1{font-size:45px;font-weight:700;letter-spacing:.5px;line-height:1.05}
.hero .tagline{font-size:24px;font-weight:600;margin-top:2px}
.hero .claim{font-size:14px;font-weight:600;color:var(--yellow);margin-top:8px}
.hero .claim+.claim{margin-top:9px}
.call-front{position:absolute;left:26px;bottom:13px;font-size:22px;font-weight:700;color:var(--ink)}
.offer{position:absolute;left:0;width:100%;text-align:center}
.offer h2{font-size:36px;font-weight:700;color:var(--royal);letter-spacing:.3px;margin-top:263px}
.offer p{font-size:22px;font-weight:600;color:var(--sky);margin-top:4px}
.steps{position:absolute;left:22px;top:357px;width:528px;display:grid;grid-template-columns:259px 259px;column-gap:10px;row-gap:19px}
.step{height:58px;background:var(--ice);display:flex;align-items:center;border-radius:29px 0 0 29px}
.step-icon{width:58px;height:58px;border-radius:50%;background:var(--ice);display:flex;align-items:center;justify-content:center;flex:none;position:relative}
.step-icon::before{content:"";position:absolute;inset:5px;border-radius:50%;background:#fff}
.step-icon svg{position:relative}
.step p{font-size:11.5px;line-height:1.25;color:#111;padding:0 6px 0 2px}
.back .brand-name{left:0;width:100%;justify-content:center;top:560px;font-size:44px;gap:14px}
.back .brand-dot{width:26px;height:26px}
.call-back{position:absolute;left:0;width:100%;text-align:center;top:662px;font-size:28px;font-weight:700;color:var(--royal)}
.web-band{position:absolute;left:0;bottom:0;width:100%;height:31px;background:linear-gradient(90deg,var(--royal) 0%,var(--brand) 60%,var(--teal) 100%);color:#fff;text-align:center;font-size:16px;letter-spacing:3px;line-height:31px}
</style>
</head>
<body>
<span class="side-label" style="left:284px">FRONT</span>
<span class="side-label" style="left:915px">BACK</span>

<section class="panel front">
  <svg class="layer" width="570" height="737" viewBox="0 0 570 737">
    <defs>
      <linearGradient id="heroBlue" x1="0" y1="0" x2="1" y2="0.3">
        <stop offset="0" stop-color="#1340c8"/><stop offset=".55" stop-color="#2f8fe0"/><stop offset="1" stop-color="#46f0d8"/>
      </linearGradient>
      <linearGradient id="washerTones" x1="0" y1="0" x2="1" y2="1">
        <stop offset="0" stop-color="#e9e6c8"/><stop offset=".45" stop-color="#c9d9e2"/><stop offset="1" stop-color="#8fb6cc"/>
      </linearGradient>
    </defs>
    <rect x="0" y="0" width="570" height="510" fill="url(#heroBlue)"/>
    <polygon points="0,0 0,250 96,211 14,129 30,129" fill="#46e6e8"/>
    <polygon points="0,129 0,250 96,212" fill="#6fece8"/>
    <polygon points="10,128 96,212 110,205 30,128" fill="#173b46"/>
  </svg>
  <div class="photo" role="img" aria-label="Photo of a row of front-loading laundromat washers with open glass doors" style="left:150px;top:0;width:420px;height:312px;background:linear-gradient(135deg,#f2f0d8 0%,#d6e2e6 45%,#9fc2d6 100%);clip-path:polygon(25% 0,100% 0,100% 100%,50% 100%,0 45%)"></div>
  <svg class="layer" width="570" height="737" viewBox="0 0 570 737">
    <path d="M150 228 L570 228 L570 312 L310 312 Q250 312 200 290 Z" fill="#5ee8dc" opacity=".8"/>
    <path d="M0 0 H320 L240 100 Q215 130 170 130 H0 Z" fill="#2150e0"/>
    <path d="M0 0 H312 L232 96 Q210 122 168 122 H0 Z" fill="#fff"/>
    <path d="M0 490 H340 Q420 490 480 545 L570 620 V737 H0 Z" fill="#13237a"/>
    <path d="M0 490 H330 Q405 492 465 548 L570 645 V737 H0 Z" fill="#fff"/>
    <path d="M0 590 Q70 580 110 630 Q150 700 230 716 Q400 737 570 710 V737 H0 Z" fill="#aef7f0"/>
    <path d="M430 737 Q500 700 570 690 V737 Z" fill="#46ecd8"/>
  </svg>
  <div class="brand-name"><span class="brand-dot"></span>Fold Harbor</div>
  <div class="outsource">
    <h2>Outsource Laundry.</h2>
    <p>Spend time on what’s most important!</p>
  </div>
  <div class="hero">
    <h1>FOLD HARBOR</h1>
    <p class="tagline">Jackson’s Premier Laundry Service</p>
    <p class="claim">Mississippi’s most Advanced &amp; Professional Laundry Service</p>
    <p class="claim">Instant Pickup &amp; Delivery System</p>
  </div>
  <div class="photo" role="img" aria-label="Photo of colourful clothes flying into a front-loading washing machine" style="left:212px;top:515px;width:358px;height:222px;background:radial-gradient(ellipse at 40% 55%,#3fc7b0 0%,#e66b4f 35%,#4a6fb5 60%,rgba(230,230,230,.9) 85%,rgba(255,255,255,0) 100%)"></div>
  <p class="call-front">call us at 555-304-2186</p>
</section>

<section class="panel back">
  <svg class="layer" width="570" height="737" viewBox="0 0 570 737">
    <defs>
      <linearGradient id="cornerBlue" x1="0" y1="0" x2="1" y2="0">
        <stop offset="0" stop-color="#4aa8f0"/><stop offset="1" stop-color="#0a14d8"/>
      </linearGradient>
    </defs>
    <path d="M0 0 H160 Q110 10 90 60 Q70 100 0 84 Z" fill="#46ece4"/>
    <path d="M380 0 H570 V106 H500 Q450 100 420 50 Z" fill="url(#cornerBlue)"/>
  </svg>
  <div class="photo" role="img" aria-label="Photo of a white and blue delivery van wrapped with laundry pickup and delivery graphics" style="left:28px;top:60px;width:518px;height:196px;border-radius:40px 60px 30px 30px;background:linear-gradient(90deg,#1e78e0 0%,#4aa6f0 35%,#f4f6f8 55%,#f4f6f8 75%,#2a70e0 100%)"></div>
  <div class="offer">
    <h2>FREE Pickup &amp; Delivery</h2>
    <p>Residential &amp; Commercial Services</p>
  </div>
  <div class="steps">
    <div class="step">
      <div class="step-icon"><svg width="38" height="38" viewBox="0 0 38 38"><circle cx="19" cy="19" r="17" fill="none" stroke="var(--navy)" stroke-width="2.5"/><path d="M19 19 L19 9 M19 19 L27 15" stroke="var(--navy)" stroke-width="2.5" stroke-linecap="round"/></svg></div>
      <p>Schedule a pickup - feel free to leave your bag where our driver can get to it.</p>
    </div>
    <div class="step">
      <div class="step-icon"><svg width="40" height="28" viewBox="0 0 40 28"><path d="M2 20 V5 H24 L32 12 H37 V20 Z" fill="none" stroke="var(--navy)" stroke-width="2"/><circle cx="10" cy="21" r="3.5" fill="#fff" stroke="var(--navy)" stroke-width="2"/><circle cx="30" cy="21" r="3.5" fill="#fff" stroke="var(--navy)" stroke-width="2"/></svg></div>
      <p>Our driver will pickup your clothes at the scheduled time.</p>
    </div>
    <div class="step">
      <div class="step-icon"><svg width="28" height="36" viewBox="0 0 28 36"><rect x="1.5" y="1.5" width="25" height="33" rx="2" fill="none" stroke="var(--navy)" stroke-width="2"/><line x1="1.5" y1="9" x2="26.5" y2="9" stroke="var(--navy)" stroke-width="1.5"/><circle cx="14" cy="21" r="7.5" fill="none" stroke="var(--navy)" stroke-width="2"/><path d="M7 22 Q14 26 21 22 A7 7 0 0 1 7 22Z" fill="var(--brand)"/></svg></div>
      <p>Your clothes are expertly cleaned by our team of laundry professionals.</p>
    </div>
    <div class="step">
      <div class="step-icon"><svg width="40" height="36" viewBox="0 0 40 36"><path d="M20 10 Q20 4 23 4 Q26 4 25 7 M20 10 L3 22 H37 Z" fill="none" stroke="var(--navy)" stroke-width="2" stroke-linejoin="round"/><rect x="9" y="22" width="22" height="11" fill="none" stroke="var(--navy)" stroke-width="2"/></svg></div>
      <p>We delivery your clean clothes back to you at your convenience!</p>
    </div>
  </div>
  <div class="brand-name"><span class="brand-dot"></span>Fold Harbor</div>
  <p class="call-back">CALL : 555-304-2186</p>
  <div class="web-band">www.foldharborlaundry.example</div>
</section>
</body>
</html>
```